Namecard and logo for New startup cloud communication company

We need name card and logo deign for our company

company name Bex Tamarind Pte Ltd
Its a cloud base company offering IP PBX communication solutions
Young start up company base in Singapore with experience in asterisk solutions

We require the design to be unique and updated
to incorporate Bex and Cloud into the design.

Industry/Entity Type

Communication

Contact Information for Business Card

We require the following on name card

Company name
Name
Company address
Mobile Number and main line with ext
email address
website address

Font styles to use
Sans Serif

```html
<!DOCTYPE html>
<html lang="en">
<head>
<meta charset="utf-8">
<title>Bex Tamarind Pte Ltd — Business Card</title>
<link rel="stylesheet" href="https://fonts.googleapis.com/css2?family=Open+Sans:wght@400;600;700&display=swap">
<style>
  :root {
    --page: #e9e9e9;
    --card-dark: #3b3b3d;
    --card-dark-deep: #2c2c2e;
    --card-light: #ffffff;
    --brand-blue: #1aa3d9;
    --ink: #2e2e30;
    --ink-soft: #555558;
    --band-grey: #4a4a4c;
    --line-grey: #bdb8b4;
    --divider: #9a9a9a;
  }
  * { margin: 0; padding: 0; box-sizing: border-box; }
  html, body {
    width: 1200px; height: 676px; overflow: hidden;
    background: var(--page);
    font-family: "Open Sans", Arial, sans-serif;
  }
  .stage {
    position: relative; width: 1200px; height: 676px;
    display: flex; align-items: center; justify-content: center; gap: 40px;
  }
  .card {
    position: relative; width: 520px; height: 297px; overflow: hidden;
    box-shadow: 0 10px 24px rgba(0,0,0,0.18);
  }

  /* Back of card */
  .card-back { background: var(--card-dark); }
  .card-back .photo {
    position: absolute; right: 0; top: 0; width: 68%; height: 100%;
    background: radial-gradient(ellipse at 55% 50%, #5b5b5e 0%, #47474a 45%, var(--card-dark) 80%);
    opacity: 0.9;
  }
  .card-back .brand {
    position: absolute; left: 40px; top: 58px;
    display: flex; align-items: center; gap: 12px;
    color: #ffffff;
  }

  /* Shared brand lockup */
  .brand-dot {
    width: 44px; height: 44px; border-radius: 50%;
    background: var(--brand-blue); flex: none;
  }
  .brand-name { font-weight: 700; line-height: 1; }
  .brand-name .big { display: block; font-size: 40px; letter-spacing: 1px; }
  .brand-name .small { display: block; font-size: 13px; margin-top: 4px; }

  /* Front of card */
  .card-front { background: var(--card-light); }
  .card-front .brand {
    position: absolute; left: 38px; top: 62px;
    display: flex; align-items: center; gap: 12px;
    color: var(--ink);
  }
  .card-front .divider {
    position: absolute; left: 262px; top: 62px; width: 1px; height: 118px;
    background: var(--divider);
  }
  .contacts {
    position: absolute; left: 278px; top: 78px; list-style: none;
    font-size: 13px; color: var(--ink); line-height: 1;
  }
  .contacts li { display: flex; align-items: center; gap: 7px; height: 17px; }
  .contacts .icon {
    width: 12px; height: 12px; background: var(--brand-blue); border-radius: 2px;
    display: flex; align-items: center; justify-content: center; flex: none;
  }
  .contacts .icon svg { width: 8px; height: 8px; fill: #fff; }
  .contacts .web { padding-left: 0; }
  .card-front .waves { position: absolute; left: 0; bottom: 0; width: 520px; height: 170px; }
</style>
</head>
<body>
<main class="stage">

  <section class="card card-back" aria-label="Business card back">
    <div class="photo" role="img" aria-label="Faded photograph of network cabling and hands working on telephone equipment"></div>
    <div class="brand">
      <span class="brand-dot"></span>
      <span class="brand-name"><span class="big">Bex</span><span class="small">Tamarind Pte Ltd</span></span>
    </div>
  </section>

  <section class="card card-front" aria-label="Business card front">
    <div class="brand">
      <span class="brand-dot"></span>
      <span class="brand-name"><span class="big">Bex</span><span class="small">Tamarind Pte Ltd</span></span>
    </div>
    <div class="divider"></div>
    <ul class="contacts">
      <li><span class="icon"><svg viewBox="0 0 10 10"><path d="M2 1h2l1 2.5-1.2 1a5 5 0 0 0 1.7 1.7l1-1.2L9 6v2a1 1 0 0 1-1 1A7 7 0 0 1 1 2a1 1 0 0 1 1-1z"/></svg></span>0123 456 789</li>
      <li><span class="icon"><svg viewBox="0 0 10 10"><rect x="3" y="0.5" width="4" height="9" rx="0.8"/></svg></span>0123 456 789</li>
      <li><span class="icon"><svg viewBox="0 0 10 10"><rect x="1" y="3" width="8" height="5"/><rect x="3" y="1" width="4" height="2"/></svg></span>0123 456 789</li>
      <li><span class="icon"><svg viewBox="0 0 10 10"><path d="M1 2.5h8v5H1z M1 2.5l4 3 4-3" stroke="#1aa3d9" stroke-width="0.8"/></svg></span>hello@bextamarind.sg</li>
      <li class="web">www.bextamarind.sg</li>
    </ul>
    <svg class="waves" viewBox="0 0 520 170" preserveAspectRatio="none" aria-hidden="true">
      <path d="M0 40 C 90 10, 170 20, 250 60 S 420 150, 520 120 L520 170 L0 170 Z" fill="var(--band-grey)"/>
      <path d="M0 36 C 90 6, 170 16, 250 56 S 420 146, 520 114" fill="none" stroke="var(--brand-blue)" stroke-width="6"/>
      <path d="M0 46 C 90 16, 170 26, 250 66 S 420 156, 520 126" fill="none" stroke="var(--line-grey)" stroke-width="4"/>
    </svg>
  </section>

</main>
</body>
</html>
```